Web redesign for Asian (IndoPak) based private equity firm

Redesign TLVholdings.com.
New site to be done on Wordpress. No flash, responsive. Keep logo. Home page, news, team, portfolio, contact us. Portfolio will be case study based so we will have some next about an industry like infrastructure and then Have logos below. Use existing images and others from Indian stock photo sites (will pay for those so use placeholders). Home page should have news feed and video front and center. Images should have eye contact. Looking for clean and simple design .

Sites we like
http://www.wdfm.com- use of video highlight

Leaflet.in
A magazine that I find very easy to read and scroll down
Allows for both text /photo and video

Target Market(s)

Private equity

Industry/Entity Type

Financial Service

Coding

Coded - Design and coding required

Number of Pages Required

5+ page

Font styles to use
Serif
Sans Serif

Colors
3377b5
85acd3

Requirements
Must have
• Responsive, video highlight, image use, existing logo, contact us, open page design . Use existing color
Nice to have
• Connect news story to content on page using tags. Pop over for team bios, custom font
Should not have
• Flash, no need for inline CSS on the content pages except absolutely necessary. No rigid content types

```html
<!DOCTYPE html>
<html lang="en">
<head>
<meta charset="utf-8">
<title>TLV Holdings — Growth Capital</title>
<link rel="stylesheet" href="https://fonts.googleapis.com/css2?family=Lora:wght@400;700&family=Open+Sans:wght@400;600;700&display=swap">
<style>
:root{
  --brand:#3377b5;
  --brand-light:#85acd3;
  --navy:#1f3f8a;
  --ink:#222;
  --muted:#8a8a8a;
  --rule:#dcdcdc;
  --card:#f2f2f2;
  --footer:#2b2b2b;
  --white:#fff;
  --accent:#e8622a;
}
*{box-sizing:border-box;margin:0;padding:0}
html,body{width:1200px;height:2314px;overflow:hidden}
body{background:var(--white);font-family:"Open Sans",Arial,sans-serif;color:var(--ink);position:relative}
.site-header{position:absolute;top:0;left:0;width:1200px;height:71px;display:flex;align-items:center;justify-content:space-between;padding:0 133px}
.brand{display:flex;align-items:center;gap:10px;font-family:"Lora",Georgia,serif;color:var(--navy);font-size:24px;font-weight:700}
.brand-mark{width:14px;height:14px;background:var(--navy)}
.main-nav{display:flex;gap:28px;font-size:12px;text-transform:uppercase;color:#555}
.main-nav .active{color:var(--navy)}
.hero{position:absolute;top:71px;left:0;width:1200px;height:415px;background:radial-gradient(ellipse at 35% 30%,#3a73cc 0%,#245cb8 40%,#163f96 75%,#0d3380 100%);display:flex;flex-direction:column;align-items:center;justify-content:center}
.hero-title{font-family:"Open Sans",sans-serif;font-weight:700;color:var(--white);font-size:27px;line-height:34px;text-align:center;text-transform:uppercase;margin-top:-30px}
.hero-btn{margin-top:14px;border:1px solid var(--white);color:var(--white);font-size:11px;font-weight:600;text-transform:uppercase;padding:11px 16px}
.hero-arrow{position:absolute;top:195px;width:24px;height:34px;background:rgba(0,0,0,.35);display:flex;align-items:center;justify-content:center}
.hero-arrow.prev{left:0}.hero-arrow.next{right:0}
.section-title{font-family:"Lora",Georgia,serif;font-weight:700;color:var(--navy);font-size:23px;text-transform:uppercase;position:absolute;top:536px}
.portfolio-card{position:absolute;top:585px;left:133px;width:216px;height:185px;background:var(--card);padding:16px 18px}
.portfolio-logo{display:block;width:57px;height:57px;border-radius:50%;background:var(--accent)}
.portfolio-name{font-family:"Lora",serif;color:var(--navy);font-size:13px;line-height:17px;margin-top:33px;white-space:nowrap}
.portfolio-sector{font-size:9px;line-height:14px;margin-top:6px;color:#333}
.search{position:absolute;top:785px;left:133px;width:216px;height:39px;background:var(--brand-light);display:flex;align-items:center;justify-content:space-between;padding:0 16px;color:var(--white);font-size:11px}
.news{position:absolute;top:583px;left:380px;width:687px}
.news-item{position:relative;height:208px;border-bottom:1px solid var(--rule)}
.news-text{position:absolute;left:0;top:0;width:442px;height:100%}
.news-date{font-family:"Lora",serif;color:var(--navy);font-size:13px;line-height:18px;margin-top:4px}
.news-title{font-size:16px;font-weight:400;line-height:22px;margin-top:3px;color:#111}
.news-title.single{margin-top:16px}
.news-body{font-size:9.6px;line-height:17.5px;color:var(--muted);margin-top:8px}
.news-title.single + .news-body{margin-top:14px}
.read-more{position:absolute;top:159px;left:0;font-size:9.5px;text-transform:uppercase;color:#333}
.news-image{position:absolute;right:0;top:0;width:217px;height:170px}
.video{position:absolute;top:1626px;left:380px;width:687px;height:359px;background:linear-gradient(180deg,#10182a 0%,#1e2236 30%,#4b3c52 50%,#7a3226 75%,#4a1a14 100%);display:flex;align-items:center;justify-content:center}
.load-more{position:absolute;top:2016px;left:659px;width:129px;height:49px;border:1px solid #cfcfcf;color:#999;font-size:14px;display:flex;align-items:center;justify-content:center}
.newsletter{position:absolute;top:2098px;left:0;width:1200px;height:95px;background:var(--brand);display:flex;align-items:center;padding-left:261px}
.newsletter h2{font-family:"Lora",serif;font-weight:400;color:var(--white);font-size:32px;margin-right:16px}
.newsletter .email{width:239px;height:43px;background:var(--white);font-size:11px;color:#888;display:flex;align-items:center;padding-left:16px}
.newsletter .subscribe{width:104px;height:43px;background:#1a1a1a;color:var(--white);font-size:12px;display:flex;align-items:center;justify-content:center}
.site-footer{position:absolute;top:2193px;left:0;width:1200px;height:121px;background:var(--footer);padding:38px 133px;color:#aaa;font-size:10.5px}
.footer-nav span{margin:0 6px}
.copyright{margin-top:14px}
.social{position:absolute;right:133px;top:43px;display:flex;gap:9px}
.social span{width:34px;height:34px;border-radius:50%;background:#d8d8d8}
</style>
</head>
<body>
<header class="site-header">
  <div class="brand"><span class="brand-mark"></span>TLV Holdings</div>
  <nav class="main-nav"><span class="active">Home</span><span>Profile</span><span>Team</span><span>Approach</span><span>News</span><span>Portfolio</span><span>Contact</span></nav>
</header>

<section class="hero" role="img" aria-label="Trader's monitors showing market data tables and charts, tinted blue">
  <h1 class="hero-title">Curabitur quis leo mattis<br>malesuada quam</h1>
  <span class="hero-btn">Read more</span>
  <span class="hero-arrow prev"><svg width="10" height="16"><path d="M8 1 L2 8 L8 15" fill="none" stroke="#fff" stroke-width="1.5"/></svg></span>
  <span class="hero-arrow next"><svg width="10" height="16"><path d="M2 1 L8 8 L2 15" fill="none" stroke="#fff" stroke-width="1.5"/></svg></span>
</section>

<h2 class="section-title" style="left:133px">Portfolio</h2>
<h2 class="section-title" style="left:380px">News and Events</h2>

<div class="portfolio-card">
  <span class="portfolio-logo"></span>
  <div class="portfolio-name">Vela Communications Ltd.</div>
  <div class="portfolio-sector">Consumer Services<br>Telecommunications and Information<br>Technology</div>
</div>
<div class="search">Search
  <svg width="12" height="12"><circle cx="5" cy="5" r="3.8" fill="none" stroke="#fff" stroke-width="1.6"/><path d="M8 8 L11 11" stroke="#fff" stroke-width="1.8"/></svg>
</div>

<div class="news">
  <article class="news-item">
    <div class="news-text">
      <div class="news-date">23 march, 2017</div>
      <h3 class="news-title">Exclusive Interview of Mr. Rohan Mehra in Asia Capital Review (ACR) magazine</h3>
      <p class="news-body">Morbi ac facilisis massa. Etiam egestas dolor ac eros hendrerit eleifend. Donec luctus eget leo in semper. Aenean rutrum iaculis lectus, et aliquet lorem viverra a. Phasellus aliquam posuere lacus, eu scelerisque justo aliquam ac. Nullam rhoncus nulla at sagittis ullamcorp&shy;er. Mauris vel tempus nisi. Suspendisse potenti. Nam quis justo enim.</p>
      <span class="read-more">Read more &#187;</span>
    </div>
    <div class="news-image" role="img" aria-label="Magazine cover with an interview quote and portrait" style="background:linear-gradient(110deg,#1d3f8f 0%,#244a9c 55%,#d9822c 70%,#6a5a6a 85%,#3a3a5a 100%)"></div>
  </article>
  <article class="news-item">
    <div class="news-text">
      <div class="news-date">23 march, 2017</div>
      <h3 class="news-title single">Vikram Thomas shares Pre-Budget views</h3>
      <p class="news-body">Morbi ac facilisis massa. Etiam egestas dolor ac eros hendrerit eleifend. Donec luctus eget leo in semper. Aenean rutrum iaculis lectus, et aliquet lorem viverra a. Phasellus aliquam posuere lacus, eu scelerisque justo aliquam ac. Nullam rhoncus nulla at sagittis ullamcorp&shy;er. Mauris vel tempus nisi. Suspendisse potenti.</p>
      <span class="read-more">Read more &#187;</span>
    </div>
    <div class="news-image" role="img" aria-label="Telecom tower in a green field under blue sky" style="background:linear-gradient(180deg,#8fb8e0 0%,#c3d8ec 62%,#7fa35a 76%,#4f7a32 100%)"></div>
  </article>
  <article class="news-item">
    <div class="news-text">
      <div class="news-date">23 march, 2017</div>
      <h3 class="news-title single">Vikram Thomas on Budget hopes</h3>
      <p class="news-body">Morbi ac facilisis massa. Etiam egestas dolor ac eros hendrerit eleifend. Donec luctus eget leo in semper. Aenean rutrum iaculis lectus, et aliquet lorem viverra a. Phasellus aliquam posuere lacus, eu scelerisque justo aliquam ac. Nullam rhoncus nulla at sagittis ullamcorp&shy;er. Mauris vel tempus nisi. Suspendisse potenti.</p>
      <span class="read-more">Read more &#187;</span>
    </div>
    <div class="news-image" role="img" aria-label="Workers welding metal in a factory with sparks" style="background:linear-gradient(160deg,#4a5666 0%,#6a5e54 45%,#9a7050 70%,#3a2e28 100%)"></div>
  </article>
  <article class="news-item">
    <div class="news-text">
      <div class="news-date">23 march, 2017</div>
      <h3 class="news-title">What the budget must really do to boost investment senti-<br>ment</h3>
      <p class="news-body">Morbi ac facilisis massa. Etiam egestas dolor ac eros hendrerit eleifend. Donec luctus eget leo in semper. Aenean rutrum iaculis lectus, et aliquet lorem viverra a. Phasellus aliquam posuere lacus, eu scelerisque justo aliquam ac. Nullam rhoncus nulla at sagittis ullamcorp&shy;er. Mauris vel tempus nisi. Suspendisse potenti. Nam quis justo enim.</p>
      <span class="read-more">Read more &#187;</span>
    </div>
    <div class="news-image" role="img" aria-label="Child learning to play a guitar in a classroom" style="background:linear-gradient(135deg,#8a6e52 0%,#bd9c78 50%,#6e5038 100%)"></div>
  </article>
  <article class="news-item">
    <div class="news-text">
      <div class="news-date">23 march, 2017</div>
      <h3 class="news-title">Sanjay Kapoor spoke at Growth Investors Forum on<br>"Early Vs Late Stage : Where is the money?"</h3>
      <p class="news-body">Morbi ac facilisis massa. Etiam egestas dolor ac eros hendrerit eleifend. Donec luctus eget leo in semper. Aenean rutrum iaculis lectus, et aliquet lorem viverra a. Phasellus aliquam posuere lacus, eu scelerisque justo aliquam ac. Nullam rhoncus nulla at sagittis ullamcorp&shy;er. Mauris vel tempus nisi. Suspendisse potenti. Nam quis justo enim.</p>
      <span class="read-more">Read more &#187;</span>
    </div>
    <div class="news-image" role="img" aria-label="Professionals walking through an open-plan office" style="background:linear-gradient(180deg,#e0e4e8 0%,#b8c0c8 50%,#6e7884 100%)"></div>
  </article>
</div>

<div class="video" role="img" aria-label="Video still of a conference stage with red carpet and speaker panels">
  <svg width="48" height="48"><circle cx="24" cy="24" r="24" fill="#fff"/><path d="M19 14 L34 24 L19 34 Z" fill="#111"/></svg>
</div>

<span class="load-more">Load more</span>

<section class="newsletter">
  <h2>Newsletter Subscribe</h2>
  <span class="email">Email Address</span>
  <span class="subscribe">SUBSCRIBE</span>
</section>

<footer class="site-footer">
  <div class="footer-nav">Home<span>|</span>Profile<span>|</span>Team<span>|</span>Approach<span>|</span>News<span>|</span>Portfolio<span>|</span>Contact</div>
  <div class="copyright">Copyright &copy; 2016&nbsp; Company name.&nbsp; All rights reserved.</div>
  <div class="social"><span></span><span></span></div>
</footer>
</body>
</html>
```